Copperleaf Motorized Shade Business Card

Hello, we've had our logo made. Now we are looking for a clean and cool looking business card. One side can just be the logo with any design elements that might look good with it. The other side will be Name, Phone Number and Email. There will not be an address on the card.

```html
<!DOCTYPE html>
<html lang="en">
<head>
<meta charset="UTF-8">
<title>Copperleaf Motorized Shade Business Card</title>
<link rel="stylesheet" href="https://fonts.googleapis.com/css2?family=Oswald:wght@500&family=Hind:wght@400&display=swap">
<style>
  :root {
    --backdrop: #9b9b9b;
    --navy: #003b75;
    --card-light: #e3e3e3;
    --white: #ffffff;
    --sun: #f6bb1c;
    --sky: #2ea3dc;
    --text-grey: #4a4a4a;
  }
  html, body {
    margin: 0;
    padding: 0;
    width: 1200px;
    height: 900px;
    overflow: hidden;
    background: var(--backdrop);
  }
  .canvas {
    position: relative;
    width: 1200px;
    height: 900px;
  }
  .card {
    position: absolute;
    left: 363px;
    width: 474px;
    height: 271px;
    border-radius: 13px;
  }
  .card-front {
    top: 145px;
    background: var(--navy);
    display: flex;
    align-items: center;
    justify-content: center;
  }
  .brand {
    display: flex;
    align-items: center;
    gap: 10px;
    margin-top: -10px;
  }
  .brand-dot {
    width: 14px;
    height: 14px;
    border-radius: 50%;
    background: var(--sun);
  }
  .brand-name {
    font-family: "Oswald", sans-serif;
    font-weight: 500;
    font-size: 24px;
    letter-spacing: 0.5px;
    text-transform: uppercase;
    color: var(--white);
  }
  .card-back {
    top: 484px;
    background: var(--card-light);
  }
  .person {
    position: absolute;
    right: 248px;
    top: 113px;
    text-align: right;
  }
  .person-name {
    font-family: "Oswald", sans-serif;
    font-weight: 500;
    font-size: 18px;
    line-height: 20px;
    color: var(--navy);
    text-transform: uppercase;
    letter-spacing: -0.2px;
  }
  .person-role {
    font-family: "Hind", sans-serif;
    font-size: 11.5px;
    line-height: 14px;
    color: var(--text-grey);
    margin-top: 3px;
  }
  .divider {
    position: absolute;
    left: 236px;
    top: 113px;
    width: 1.5px;
    height: 42px;
    background: var(--sun);
  }
  .contact-list {
    position: absolute;
    left: 248px;
    top: 112px;
    margin: 0;
    padding: 0;
    list-style: none;
    font-family: "Hind", sans-serif;
    font-size: 11px;
    line-height: 15px;
    color: var(--text-grey);
  }
  .contact-list li {
    display: flex;
    align-items: center;
    gap: 6px;
  }
  .contact-list svg {
    width: 9px;
    height: 9px;
    flex: none;
  }
</style>
</head>
<body>
<div class="canvas">
  <section class="card card-front">
    <div class="brand">
      <span class="brand-dot"></span>
      <span class="brand-name">Copperleaf Motorized Shade</span>
    </div>
  </section>

  <section class="card card-back">
    <div class="person">
      <div class="person-name">Marcus Hale</div>
      <div class="person-role">President/Owner</div>
    </div>
    <div class="divider"></div>
    <ul class="contact-list">
      <li>
        <svg viewBox="0 0 10 10" aria-hidden="true"><path d="M2 0.8 L3.6 2.6 L2.8 3.6 Q4 5.8 6.2 7 L7.3 6.2 L9.2 7.8 L8 9.2 Q4.2 9 1.2 5 Q0 2.4 2 0.8 Z" fill="var(--sky)"/></svg>
        <span>555.214.0376</span>
      </li>
      <li>
        <svg viewBox="0 0 10 10" aria-hidden="true"><rect x="0.5" y="2" width="9" height="6" fill="var(--sky)"/><path d="M0.5 2 L5 5.5 L9.5 2" stroke="var(--card-light)" stroke-width="0.9" fill="none"/></svg>
        <span>info@copperleafshade.com</span>
      </li>
      <li>
        <svg viewBox="0 0 10 10" aria-hidden="true"><circle cx="5" cy="5" r="4.3" fill="var(--sky)"/><path d="M0.7 5 H9.3 M5 0.7 Q2.6 5 5 9.3 M5 0.7 Q7.4 5 5 9.3" stroke="var(--card-light)" stroke-width="0.6" fill="none"/></svg>
        <span>www.copperleafshade.com</span>
      </li>
    </ul>
  </section>
</div>
</body>
</html>
```